Website design for Cambridge based systematic hedge fund

We have run previous craftmosaic competitions to design our company logo, business cards and the styling of our presentation deck (see attached files).
As the final step we are looking to get a website designed that is thematically consistent with these existing elements of our branding.
You can find some of our competitors websites below:
https://www.quelmarsh.example/
https://www.fenloor.example/
https://www.pyvart.example/
https://www.dulvet.example/
https://www.orbelmfunds.example/
https://www.valtrigo.example/
https://www.meskilfunds.example/home
We would like to have a website that works well on both mobile devices and desktops. Either just as one page that can be scrolled down, with links at the top that skips to certain sections, or a few separate pages that can be navigated by a top menu.
It should look professional, we are not after lots of animations or unnecessary transitions, and in particular the website must be smooth to navigate. We would like to avoid having peoples of people, we are happy to make use of elements from the presentation (for example the style of the cover slide, or the section slides with the faded bridge in the background), or 'financial' style images.
We would like to have the following sections for now. For some of these some example text has been provided, final text may change but it will be of similar length. For the other sections we are happy to just have template text for now. At the moment we are mainly interested to see styles/layouts as words can be added easily afterwards:
1) We will need a disclaimer pop up the first time someone visits the site (see for example the meskilfunds example).
2) Top page - company name, then in larger text "Bringing AI and Statistical Inference to Financial Markets", and somewhere in smaller text "Harlow Vectors is a quantitative asset manager with the singular focus of delivering algorithmic strategies that work"
3) "About us" section: will describe us as a company, details our approach, company values, and explains the company logo.
Example text:
"We deliver consistent alpha across liquid markets through the application of proprietary IP in Bayesian inference, machine learning and artificial intelligence. We are a multi-disciplinary team founded by experienced finance professionals from premier institutions, leading academics from the Thornbury Stellar Unit at Ashmere College and world-class software engineers.
Our logo portrays a sillhoute of the lattice walkway at Ashmere College. Our unique scientific approach allows us to bridge cutting-edge mathematical research and computing expertise with financial knowledge to bring algorithmns that work to liquid markets"
4) Hiring section, detailing our culture, what we are looking for.
Example text:
"We are always looking for exceptional talent to join our entrepreneurial team. We are looking for individuals who are creative thinkers, can demonstrate analytical rigour and are passionate about the intersection of science, finance and technology.
We prioritise having a company culture that promotes sharing ideas in a safe, collaborative research environment. We make sure that every member of the team has the oppertunity to explore their own ideas through weekly 'innovation time', and ensure that everyone gets the support they need to continue to grow as individuals within the company."
5) A section for news/press releases
6) Contact us area at the bottom with office location and email. We will need to list 3 addresses for our Cambridge, London and Singapore offices, along with a couple of contact emails or phone numbers
7) A client login button at the top that will take them to a different website (unrelated to this one).

```html
<!DOCTYPE html>
<html lang="en">
<head>
<meta charset="utf-8">
<title>Harlow Vectors — Website Design, Desktop and Mobile</title>
<link rel="stylesheet" href="https://fonts.googleapis.com/css2?family=Montserrat:wght@400;600;700;800;900&family=Poppins:wght@300;400;500;600&display=swap">
<style>
:root{
  --board:#d7d7da;
  --ink:#0a0b0f;
  --night:#050e19;
  --navy:#0a2440;
  --blue:#2d6fb6;
  --blue-light:#4b93dc;
  --blue-deep:#163f74;
  --mauve:#9c5a7c;
  --text:#3a3d44;
  --muted:#8a8f99;
  --white:#ffffff;
  --tile:#1b1c21;
}
*{box-sizing:border-box;margin:0;padding:0}
html,body{width:1200px;height:4705px;overflow:hidden}
body{background:var(--board);font-family:"Poppins",sans-serif;color:var(--text);position:relative}
.board-label{position:absolute;top:40px;font-family:"Montserrat",sans-serif;font-weight:700;font-size:12px;letter-spacing:.6em;color:var(--ink)}
.board-label--desktop{left:400px}
.board-label--mobile{left:940px}

.head{font-family:"Montserrat",sans-serif;font-weight:800;color:var(--ink);letter-spacing:.12em;text-transform:uppercase}
.eyebrow{font-family:"Montserrat",sans-serif;font-weight:400;letter-spacing:.7em;text-transform:uppercase;color:var(--blue-light)}
.btn{display:inline-block;font-family:"Montserrat",sans-serif;font-weight:700;text-transform:uppercase;letter-spacing:.12em;color:var(--white);text-align:center}
.btn--mauve{background:var(--mauve)}
.btn--blue{background:var(--blue)}
.btn--white{background:var(--white);color:var(--ink)}
.wordmark{font-family:"Montserrat",sans-serif;font-weight:800;color:var(--blue-deep);letter-spacing:.04em;text-transform:uppercase;display:flex;align-items:center;gap:5px;white-space:nowrap}
.wordmark i{display:block;background:var(--blue-deep)}
.photo{position:absolute}
.photo--suit{background:linear-gradient(160deg,#1d3350 0%,#0c1828 55%,#2b5f95 100%)}
.photo--handshake{background:linear-gradient(135deg,#cfd6df 0%,#8d9bad 45%,#3f536d 100%)}
.photo--chart{background:linear-gradient(180deg,#0d2a45 0%,#114574 50%,#e08a3a 120%)}
.photo--globe{background:radial-gradient(ellipse 70% 90% at 50% 110%,#2f8fd0 0%,#0f4c7e 35%,rgba(6,20,38,0) 70%)}
.photo--particles{background:radial-gradient(ellipse 60% 70% at 70% 55%,#2a8fd8 0%,#0d3f6e 40%,rgba(4,12,22,0) 75%)}
.photo--fabric{background:linear-gradient(135deg,#1f3f78 0%,#c23a3a 60%,#e2d2a0 100%)}
.photo--desk{background:linear-gradient(135deg,#e4e6ea 0%,#b9c1cc 60%,#7d8795 100%)}
.photo--phone{background:linear-gradient(135deg,#e9eaec 0%,#a8aeb6 50%,#31353c 100%)}
.stats-box{position:absolute;background:linear-gradient(135deg,var(--blue-deep) 0%,var(--blue) 55%,var(--blue-light) 100%)}
.stat{position:absolute;color:var(--white);font-family:"Montserrat",sans-serif;font-weight:700;border-left:2px solid rgba(0,0,0,.55)}
.stat b{display:block;line-height:1}
.stat span{display:block;font-family:"Poppins",sans-serif;font-weight:400;opacity:.85}
.tile{position:absolute;background:var(--tile);color:var(--white);display:flex;flex-direction:column;align-items:center;justify-content:center;text-align:center;font-family:"Montserrat",sans-serif;font-weight:600}
.tile--active{background:var(--mauve)}
.tile svg{stroke:var(--white);fill:none;stroke-width:1.6}
.social{display:flex;gap:5px}
.social i{display:block;border-radius:50%}
.social i:nth-child(1){background:#2e5ea8}
.social i:nth-child(2){background:#b2447f}
.social i:nth-child(3){background:#2e78b8}
.field{background:rgba(255,255,255,.95)}

/* ===== DESKTOP ===== */
.desktop{position:absolute;left:90px;top:90px;width:760px;height:3906px;background:var(--white);overflow:hidden}
.d-section{position:relative;width:760px}
.d-nav{height:61px;display:flex;align-items:center;justify-content:space-between;padding:0 80px;font-family:"Montserrat",sans-serif;font-size:7px;letter-spacing:.14em;color:#555;text-transform:uppercase}
.d-nav ul{display:flex;gap:42px;list-style:none}
.d-nav .wordmark{font-size:12px}
.d-nav .wordmark i{width:7px;height:7px}
.d-login{display:flex;align-items:center;gap:4px}
.d-hero{height:480px;background:radial-gradient(ellipse 90% 70% at 50% 30%,#0b2340 0%,var(--night) 70%);color:var(--white);text-align:center;overflow:hidden}
.d-hero .photo--globe{left:0;right:0;bottom:0;height:330px}
.d-hero .eyebrow{position:absolute;top:68px;left:0;right:0;font-size:8px;color:#4c6a8c}
.d-hero h1{position:absolute;top:86px;left:0;right:0;font-family:"Montserrat",sans-serif;font-weight:700;font-size:21px;letter-spacing:.28em;line-height:1.42}
.d-hero p{position:absolute;top:186px;left:0;right:0;font-size:8px;line-height:1.6;color:#c9d4e2}
.d-hero .btn{position:absolute;top:242px;left:331px;width:98px;height:19px;line-height:19px;font-size:6.5px}
.d-scroll{position:absolute;right:78px;top:258px;width:1px;height:160px;background:rgba(255,255,255,.5)}
.d-scroll-num{position:absolute;right:70px;top:355px;font-size:11px;color:#fff;background:var(--night);padding:2px 3px}
.d-who{height:415px}
.d-who .photo{left:81px;top:-33px;width:303px;height:448px;z-index:2}
.d-who .ghost{position:absolute;left:665px;top:110px;font-family:"Montserrat",sans-serif;font-weight:800;font-size:64px;color:transparent;-webkit-text-stroke:1px #eceef2}
.d-who h2{position:absolute;left:456px;top:80px;font-size:20px;letter-spacing:.2em}
.d-who p{position:absolute;left:456px;top:118px;width:200px;font-size:8px;line-height:1.55}
.d-who .btn{position:absolute;left:456px;top:290px;width:106px;height:22px;line-height:22px;font-size:6.5px}
.d-values{height:256px}
.d-values .eyebrow{position:absolute;left:79px;top:70px;font-size:9px}
.d-values h2{position:absolute;left:79px;top:86px;font-size:42px;letter-spacing:.12em;font-weight:900}
.d-values p{position:absolute;left:79px;top:152px;width:250px;font-size:8px;line-height:1.55}
.d-values .ghost{position:absolute;left:20px;top:-10px;font-family:"Montserrat",sans-serif;font-weight:800;font-size:64px;color:transparent;-webkit-text-stroke:1px #eceef2}
.d-values .stats-box{left:387px;top:0;width:314px;height:290px;z-index:3}
.d-stat-1{left:52px;top:42px;padding-left:24px;height:58px}
.d-stat-2{left:152px;top:112px;padding-left:22px;height:50px}
.d-stat-3{left:52px;top:180px;padding-left:24px;height:58px}
.d-stat-1 b,.d-stat-3 b{font-size:30px}
.d-stat-2 b{font-size:28px}
.d-values .stat span{font-size:6px;margin-top:4px}
.d-approach{height:472px;background:var(--ink);color:var(--white);text-align:center}
.d-approach .ghost{position:absolute;left:612px;top:20px;font-family:"Montserrat",sans-serif;font-weight:800;font-size:64px;color:transparent;-webkit-text-stroke:1px #26272d}
.d-approach h2{position:absolute;left:0;right:0;top:108px;font-family:"Montserrat",sans-serif;font-weight:700;font-size:19px;letter-spacing:.26em}
.d-approach p{position:absolute;left:0;right:0;top:144px;font-size:8px;line-height:1.6;color:#c9ccd3}
.d-approach .tile{top:218px;width:109px;height:110px;font-size:6px;gap:10px}
.d-approach .btn{position:absolute;left:296px;top:382px;width:168px;height:20px;line-height:20px;font-size:6.5px}
.d-culture{height:697px}
.d-culture .photo--handshake{left:79px;top:63px;width:275px;height:323px}
.d-culture .eyebrow{position:absolute;left:408px;top:76px;font-size:9px}
.d-culture h2{position:absolute;left:408px;top:92px;font-size:42px;font-weight:900}
.d-culture .lead{position:absolute;left:408px;top:160px;width:250px;font-size:8px;line-height:1.55}
.d-culture .photo--chart{left:408px;top:304px;width:271px;height:316px}
.d-culture .body{position:absolute;left:79px;top:452px;width:250px;font-size:8px;line-height:1.55}
.d-culture .btn{position:absolute;left:79px;top:578px;width:106px;height:22px;line-height:22px;font-size:6.5px}
.d-hiring{height:415px;background:linear-gradient(90deg,#03080f 0%,#07182a 100%);overflow:hidden}
.d-hiring .photo--particles{left:200px;top:0;right:0;bottom:0}
.d-hiring .card{position:absolute;left:81px;top:66px;width:327px;height:283px;background:linear-gradient(135deg,var(--blue-deep) 0%,var(--blue) 60%,var(--blue-light) 100%);padding:40px 42px;color:var(--white)}
.d-hiring .eyebrow{font-size:8px;color:#a9cdf2}
.d-hiring h2{font-family:"Montserrat",sans-serif;font-weight:800;font-size:21px;letter-spacing:.2em;line-height:1.05;margin-top:4px}
.d-hiring p{font-size:7.5px;line-height:1.55;margin-top:14px;width:240px}
.d-hiring .btn{margin-top:16px;width:106px;height:22px;line-height:22px;font-size:6.5px}
.d-insights{height:553px}
.d-insights .ghost{position:absolute;left:175px;top:20px;font-family:"Montserrat",sans-serif;font-weight:800;font-size:64px;color:transparent;-webkit-text-stroke:1px #eceef2}
.d-insights .eyebrow{position:absolute;left:0;right:0;top:70px;text-align:center;font-size:9px}
.d-insights h2{position:absolute;left:0;right:0;top:84px;text-align:center;font-size:40px;font-weight:900}
.d-post{position:absolute;left:79px;width:310px;height:90px}
.d-post .photo{left:0;top:0;width:91px;height:87px}
.d-post h3{position:absolute;left:111px;top:20px;font-family:"Montserrat",sans-serif;font-weight:800;font-size:8px;letter-spacing:.2em;color:var(--ink)}
.d-post p{position:absolute;left:111px;top:34px;width:200px;font-size:6.5px;line-height:1.5}
.d-feature{position:absolute;left:417px;top:164px;width:258px}
.d-feature .photo{position:relative;display:block;width:258px;height:251px}
.d-feature h3{margin-top:10px;font-family:"Montserrat",sans-serif;font-weight:800;font-size:8px;letter-spacing:.2em;color:var(--ink)}
.d-feature p{margin-top:5px;font-size:6.5px;line-height:1.5}
.d-partner{height:365px;background:var(--ink);color:var(--white)}
.d-partner h2{position:absolute;left:79px;top:59px;font-family:"Montserrat",sans-serif;font-weight:700;font-size:19px;letter-spacing:.26em}
.d-office{position:absolute;top:103px;width:200px}
.d-office h3{font-family:"Montserrat",sans-serif;font-weight:700;font-size:7px;letter-spacing:.2em;margin-bottom:12px}
.contact-row{display:flex;gap:10px;margin-bottom:10px;font-size:5.5px;line-height:1.45;color:#c9ccd3}
.contact-row svg{flex:none;width:9px;height:9px;fill:none;stroke:#c9ccd3;stroke-width:1.6}
.contact-row b{display:block;color:var(--white);font-weight:500}
.d-partner .btn{position:absolute;left:79px;top:266px;width:106px;height:22px;line-height:22px;font-size:6.5px}
.d-footer{height:192px}
.d-footer .wordmark{position:absolute;left:79px;top:38px;font-size:13px}
.d-footer .wordmark i{width:8px;height:8px}
.d-footer .blurb{position:absolute;left:79px;top:64px;width:200px;font-size:6.5px;line-height:1.5}
.d-footer .social{position:absolute;left:79px;top:94px}
.d-footer .social i{width:14px;height:14px}
.d-footer small{position:absolute;left:79px;top:120px;font-size:5.5px;color:var(--muted)}
.d-links{position:absolute;left:332px;top:40px;list-style:none;font-size:6px;line-height:2.1}
.d-links li:first-child{font-family:"Montserrat",sans-serif;font-weight:700;font-size:8px;letter-spacing:.3em;color:var(--ink)}
.d-touch{position:absolute;left:437px;top:3626px;width:242px;height:240px;background:linear-gradient(135deg,var(--blue-deep) 0%,var(--blue) 60%,var(--blue-light) 100%);padding:26px 22px;z-index:5}
.d-touch h3{text-align:center;color:var(--white);font-family:"Montserrat",sans-serif;font-weight:700;font-size:9px;letter-spacing:.3em;margin-bottom:14px}
.d-touch .field{height:16px;margin-bottom:7px;border-bottom:1px solid #d5dbe3;font-size:5px;color:#aab0ba;padding:4px 6px}
.d-touch .field--area{height:82px;position:relative}
.d-touch .field--area svg{position:absolute;right:6px;bottom:6px;width:11px;height:11px;fill:var(--blue)}

/* ===== MOBILE ===== */
.mobile{position:absolute;left:910px;top:90px;width:200px;height:4553px;background:var(--white);overflow:hidden}
.m-section{position:relative;width:200px}
.m-nav{height:51px;display:flex;align-items:center;justify-content:space-between;padding:0 10px}
.m-nav .wordmark{font-size:8px}
.m-nav .wordmark i{width:5px;height:5px}
.m-burger{width:12px;height:8px;border-top:1px solid #333;border-bottom:1px solid #333;position:relative}
.m-burger::after{content:"";position:absolute;left:0;right:3px;top:3px;border-top:1px solid #333}
.m-hero{height:389px;background:radial-gradient(ellipse 90% 70% at 50% 30%,#0b2340 0%,var(--night) 70%);color:var(--white);text-align:center;overflow:hidden}
.m-hero .photo--globe{left:0;right:0;bottom:0;height:170px}
.m-hero .eyebrow{position:absolute;top:22px;left:0;right:0;font-size:4.5px;color:#4c6a8c;letter-spacing:.5em}
.m-hero h1{position:absolute;top:34px;left:0;right:0;font-family:"Montserrat",sans-serif;font-weight:700;font-size:10px;letter-spacing:.22em;line-height:1.45}
.m-hero p{position:absolute;top:118px;left:14px;right:14px;font-size:5.5px;line-height:1.5;color:#c9d4e2}
.m-hero .btn{position:absolute;top:150px;left:64px;width:72px;height:13px;line-height:13px;font-size:4.5px}
.m-hero .d-scroll-line{position:absolute;left:99px;top:200px;width:1px;height:70px;background:rgba(255,255,255,.4)}
.m-photo{height:249px}
.m-photo .photo{left:9px;top:-18px;width:182px;height:267px}
.m-who{height:222px}
.m-who h2{position:absolute;left:9px;top:26px;font-size:10px;letter-spacing:.22em}
.m-who p{position:absolute;left:9px;top:46px;width:165px;font-size:5.5px;line-height:1.5}
.m-who .btn{position:absolute;left:9px;top:168px;width:62px;height:13px;line-height:13px;font-size:4.5px}
.m-stats{height:333px}
.m-stats .stats-box{left:9px;top:0;width:182px;height:303px}
.m-stats .stat{left:24px;padding-left:16px;height:48px}
.m-stats .stat b{font-size:27px}
.m-stats .stat span{font-size:5px;margin-top:4px}
.m-values{height:167px}
.m-values .eyebrow{position:absolute;left:9px;top:14px;font-size:5px;letter-spacing:.5em}
.m-values h2{position:absolute;left:9px;top:22px;font-size:19px;font-weight:900}
.m-values p{position:absolute;left:9px;top:54px;width:150px;font-size:5.5px;line-height:1.5}
.m-approach{height:344px;background:var(--ink);color:var(--white);text-align:center}
.m-approach h2{position:absolute;left:0;right:0;top:40px;font-family:"Montserrat",sans-serif;font-weight:700;font-size:10px;letter-spacing:.26em}
.m-approach p{position:absolute;left:18px;right:18px;top:60px;font-size:5.5px;line-height:1.5;color:#c9ccd3}
.m-approach .tile{left:48px;top:152px;width:104px;height:110px;font-size:5px;gap:8px}
.m-arrow{position:absolute;top:200px;width:10px;height:14px;stroke:var(--white);fill:none;stroke-width:1.4}
.m-approach .btn{position:absolute;left:9px;top:296px;width:182px;height:13px;line-height:13px;font-size:4.5px}
.m-culture{height:706px}
.m-culture h2{position:absolute;left:9px;top:20px;font-size:19px;font-weight:900}
.m-culture .lead{position:absolute;left:9px;top:52px;width:170px;font-size:5.5px;line-height:1.5}
.m-culture .photo--handshake{left:9px;top:178px;width:120px;height:155px}
.m-culture .photo--chart{left:71px;top:310px;width:120px;height:150px}
.m-culture .body{position:absolute;left:9px;top:478px;width:170px;font-size:5.5px;line-height:1.5}
.m-culture .btn{position:absolute;left:9px;top:595px;width:62px;height:13px;line-height:13px;font-size:4.5px}
.m-hiring{height:504px;background:linear-gradient(180deg,#03080f 0%,#07182a 100%);overflow:hidden}
.m-hiring .photo--particles{left:0;right:0;top:200px;bottom:0}
.m-hiring .card{position:absolute;left:9px;top:40px;width:182px;height:226px;background:linear-gradient(135deg,var(--blue-deep) 0%,var(--blue) 60%,var(--blue-light) 100%);padding:24px 14px;color:var(--white);text-align:center}
.m-hiring .eyebrow{font-size:4.5px;color:#a9cdf2;letter-spacing:.5em}
.m-hiring h2{font-family:"Montserrat",sans-serif;font-weight:800;font-size:10px;letter-spacing:.2em;line-height:1.1;margin-top:3px}
.m-hiring p{font-size:5.5px;line-height:1.5;margin-top:10px}
.m-hiring .btn{margin-top:12px;width:70px;height:13px;line-height:13px;font-size:4.5px}
.m-insights{height:400px}
.m-insights .eyebrow{position:absolute;left:0;right:0;top:40px;text-align:center;font-size:5px;letter-spacing:.5em}
.m-insights h2{position:absolute;left:0;right:0;top:48px;text-align:center;font-size:19px;font-weight:900}
.m-insights .photo{left:9px;top:96px;width:182px;height:182px}
.m-dot{position:absolute;top:180px;width:14px;height:14px;border-radius:50%;background:var(--white);display:flex;align-items:center;justify-content:center}
.m-dot svg{width:6px;height:6px;stroke:var(--ink);fill:none;stroke-width:2}
.m-insights h3{position:absolute;left:9px;top:290px;font-family:"Montserrat",sans-serif;font-weight:800;font-size:6px;letter-spacing:.18em;color:var(--ink)}
.m-insights p{position:absolute;left:9px;top:304px;width:170px;font-size:5px;line-height:1.5}
.m-partner{height:633px;background:var(--ink);color:var(--white)}
.m-partner h2{position:absolute;left:18px;top:40px;width:160px;font-family:"Montserrat",sans-serif;font-weight:700;font-size:10px;letter-spacing:.26em;line-height:1.2}
.m-office{position:absolute;left:18px;width:165px}
.m-office h3{font-family:"Montserrat",sans-serif;font-weight:700;font-size:5.5px;letter-spacing:.2em;margin-bottom:10px}
.m-partner .contact-row{font-size:4.5px;gap:8px;margin-bottom:8px}
.m-partner .contact-row svg{width:7px;height:7px}
.m-partner .btn{position:absolute;left:18px;top:586px;width:164px;height:13px;line-height:13px;font-size:4.5px}
.m-touch{height:255px;background:var(--ink)}
.m-touch .box{position:absolute;left:9px;top:0;width:182px;height:255px;background:linear-gradient(135deg,var(--blue-deep) 0%,var(--blue) 60%,var(--blue-light) 100%);padding:24px 22px}
.m-touch h3{text-align:center;color:var(--white);font-family:"Montserrat",sans-serif;font-weight:700;font-size:7px;letter-spacing:.3em;margin-bottom:12px}
.m-touch .field{height:12px;margin-bottom:6px;font-size:4px;color:#aab0ba;padding:3px 5px}
.m-touch .field--area{height:120px;position:relative}
.m-touch .field--area svg{position:absolute;right:5px;bottom:5px;width:9px;height:9px;fill:var(--blue)}
.m-footer{height:300px}
.m-footer .wordmark{position:absolute;left:9px;top:36px;font-size:10px}
.m-footer .wordmark i{width:6px;height:6px}
.m-footer .blurb{position:absolute;left:9px;top:58px;width:150px;font-size:5px;line-height:1.5}
.m-footer .m-links{position:absolute;left:9px;top:96px;list-style:none;font-size:5px;line-height:2.2}
.m-footer .m-links li:first-child{font-family:"Montserrat",sans-serif;font-weight:700;font-size:6px;letter-spacing:.3em;color:var(--ink)}
.m-footer .social{position:absolute;left:9px;top:222px}
.m-footer .social i{width:13px;height:13px}
.m-footer small{position:absolute;left:9px;top:244px;font-size:4.5px;color:var(--muted)}
</style>
</head>
<body>

<svg width="0" height="0" style="position:absolute" aria-hidden="true">
  <defs>
    <symbol id="ico-pin" viewBox="0 0 12 12"><path d="M6 11S2 7 2 4.5a4 4 0 0 1 8 0C10 7 6 11 6 11z"/><circle cx="6" cy="4.5" r="1.3"/></symbol>
    <symbol id="ico-mail" viewBox="0 0 12 12"><rect x="1" y="2.5" width="10" height="7"/><path d="M1 2.5l5 4 5-4"/></symbol>
    <symbol id="ico-phone" viewBox="0 0 12 12"><path d="M3 1.5l2 2.5-1.2 1.3a6 6 0 0 0 2.9 2.9L8 7l2.5 2-1 1.5C5.5 10.5 1.5 6.5 1.5 2.5z"/></symbol>
    <symbol id="ico-send" viewBox="0 0 12 12"><path d="M1 6l10-5-3 10-2-4z"/></symbol>
  </defs>
</svg>

<div class="board-label board-label--desktop">DESKTOP</div>
<div class="board-label board-label--mobile">MOBILE</div>

<main class="desktop">

  <header class="d-section d-nav">
    <ul><li>Approach</li><li>Businesses</li><li>Insights</li></ul>
    <div class="wordmark"><i></i>Harlow Vectors</div>
    <ul>
      <li>Careers</li><li>Contact us</li>
      <li class="d-login"><svg width="8" height="8" viewBox="0 0 12 12" fill="none" stroke="#555" stroke-width="1.4"><circle cx="6" cy="4" r="2.5"/><path d="M1.5 11.5c.5-3 2.3-4 4.5-4s4 1 4.5 4"/></svg>Login</li>
    </ul>
  </header>

  <section class="d-section d-hero">
    <div class="photo photo--globe" role="img" aria-label="Glowing digital globe made of blue light points"></div>
    <div class="eyebrow">Harlow Vectors</div>
    <h1>BRINGING AI AND<br>STATISTICAL INFERENCE TO<br>FINANCIAL MARKETS</h1>
    <p>Harlow Vectors is a quantitative asset manager with the singular focus<br>of delivering algorithmic strategies that work</p>
    <div class="btn btn--blue">Contact us</div>
    <div class="d-scroll"></div>
    <div class="d-scroll-num">0</div>
  </section>

  <section class="d-section d-who">
    <div class="photo photo--suit" role="img" aria-label="Businessman in a dark suit holding a tablet with a glowing rising bar chart"></div>
    <div class="ghost">01</div>
    <h2 class="head">Who we are</h2>
    <p>We deliver consistent alpha across liquid markets through the application of proprietary IP in Bayesian inference, machine learning and artificial intelligence. We are a multi-disciplinary team founded by experienced finance professionals from premier institutions, leading academics from the Thornbury Stellar Unit at Ashmere College and world-class software engineers.</p>
    <div class="btn btn--mauve">Read more</div>
  </section>

  <section class="d-section d-values">
    <div class="ghost">02</div>
    <div class="eyebrow">Company</div>
    <h2 class="head">Values</h2>
    <p>Our logo portrays a silhouette of the lattice walkway at Ashmere College.</p>
    <div class="stats-box">
      <div class="stat d-stat-1"><b>200+</b><span>Team members</span></div>
      <div class="stat d-stat-2"><b>15+</b><span>Year history</span></div>
      <div class="stat d-stat-3"><b>100+</b><span>Portfolio managers</span></div>
    </div>
  </section>

  <section class="d-section d-approach">
    <div class="ghost">03</div>
    <h2>APPROACH</h2>
    <p>Our unique scientific approach allows us to bridge cutting-edge mathematical research and computing expertise<br>with financial knowledge to bring algorithms that work to liquid markets</p>
    <div class="tile tile--active" style="left:79px"><svg width="26" height="22" viewBox="0 0 26 22"><path d="M6 14a5 5 0 0 1 1-9.8A7 7 0 0 1 20 6a4 4 0 0 1 0 8z"/><path d="M9 14v5M13 14v6M17 14v5"/></svg>It starts with<br>data</div>
    <div class="tile" style="left:203px"><svg width="26" height="22" viewBox="0 0 26 22"><circle cx="7" cy="14" r="5"/><circle cx="19" cy="14" r="5"/><path d="M11 11h4M5 9l2-6h3M21 9l-2-6h-3"/></svg>Finding signals in<br>the noise</div>
    <div class="tile" style="left:327px"><svg width="24" height="24" viewBox="0 0 24 24"><path d="M11 4a9 9 0 1 0 9 9h-9z"/><path d="M14 1v9h9a9 9 0 0 0-9-9z"/></svg>Understanding<br>patterns in markets</div>
    <div class="tile" style="left:451px"><svg width="24" height="24" viewBox="0 0 24 24"><circle cx="12" cy="12" r="10"/><circle cx="12" cy="12" r="6"/><circle cx="12" cy="12" r="2"/></svg>Experienced in<br>implementation</div>
    <div class="tile" style="left:575px"><svg width="24" height="24" viewBox="0 0 24 24"><path d="M3 21h18M6 21v-6M11 21v-9M16 21v-12M3 12l6-5 5 3 7-7"/></svg>Quantitative<br>investment</div>
    <div class="btn btn--blue">Find out how we do it</div>
  </section>

  <section class="d-section d-culture">
    <div class="photo photo--handshake" role="img" aria-label="Two business people shaking hands in a bright office"></div>
    <div class="eyebrow">Our</div>
    <h2 class="head">Culture</h2>
    <p class="lead">We prioritise having a company culture that promotes sharing ideas in a safe, collaborative research environment. We make sure that every member of the team has the opportunity to explore their own ideas through weekly 'innovation time', and ensure that everyone gets the support they need to continue to grow as individuals within the company.</p>
    <div class="photo photo--chart" role="img" aria-label="Glowing candlestick stock chart on a dark blue screen"></div>
    <p class="body">Lorem ipsum is simply dummy text of the printing and typesetting industry. Lorem Ipsum has been the industry's standard dummy text ever since the 1500s, when an unknown printer took a galley of type and scrambled it to make a type specimen book. It has survived not only five centuries, but also the leap into electronic typesetting, remaining essentially unchanged. It was popularised in the 1960s.</p>
    <div class="btn btn--mauve">Our culture</div>
  </section>

  <section class="d-section d-hiring">
    <div class="photo photo--particles" role="img" aria-label="Flowing wave of blue digital particles on a dark background"></div>
    <div class="card">
      <div class="eyebrow">Hiring</div>
      <h2>HARLOW<br>VECTORS</h2>
      <p>We are always looking for exceptional talent to join our entrepreneurial team. We are looking for individuals who are creative thinkers, can demonstrate analytical rigour and are passionate about the intersection of science, finance and technology.</p>
      <div class="btn btn--white">Connect with us</div>
    </div>
  </section>

  <section class="d-section d-insights">
    <div class="ghost">04</div>
    <div class="eyebrow">Latest</div>
    <h2 class="head">Insights</h2>
    <article class="d-post" style="top:164px">
      <div class="photo photo--desk" role="img" aria-label="Desk with laptop and financial reports"></div>
      <h3>LOREM IPSUM IS SIMPLY....</h3>
      <p>Lorem ipsum is simply dummy text of the printing and typesetting industry.</p>
    </article>
    <article class="d-post" style="top:284px">
      <div class="photo photo--fabric" role="img" aria-label="Abstract folded coloured shapes"></div>
      <h3>LOREM IPSUM IS SIMPLY....</h3>
      <p>Lorem ipsum is simply dummy text of the printing and typesetting industry.</p>
    </article>
    <article class="d-post" style="top:404px">
      <div class="photo photo--desk" role="img" aria-label="Analyst working at a desk with charts"></div>
      <h3>LOREM IPSUM IS SIMPLY....</h3>
      <p>Lorem ipsum is simply dummy text of the printing and typesetting industry.</p>
    </article>
    <article class="d-feature">
      <div class="photo photo--phone" role="img" aria-label="Hands holding a phone in front of a laptop showing a stock chart"></div>
      <h3>LOREM IPSUM IS SIMPLY....</h3>
      <p>Lorem ipsum is simply dummy text of the printing and typesetting industry. Lorem ipsum has been the industry's standard dummy text ever since the 1500s, when an unknown printer.</p>
    </article>
  </section>

  <section class="d-section d-partner">
    <h2>PARTNER WITH US</h2>
    <div class="d-office" style="left:79px">
      <h3>EASTMERE OFFICE</h3>
      <div class="contact-row"><svg><use href="#ico-pin"/></svg><div><b>Location</b>42 West Mill Street, 8th Floor<br>Eastmere, Suite 8A</div></div>
      <div class="contact-row"><svg><use href="#ico-mail"/></svg><div><b>Email</b>info@harlowvectors.example</div></div>
      <div class="contact-row"><svg><use href="#ico-phone"/></svg><div><b>Call</b>+00 0100 000 114</div></div>
    </div>
    <div class="d-office" style="left:308px">
      <h3>DUNHOLT OFFICE</h3>
      <div class="contact-row"><svg><use href="#ico-pin"/></svg><div><b>Location</b>18 Fenwick Lane, 3rd Floor<br>Dunholt, Suite 3C</div></div>
      <div class="contact-row"><svg><use href="#ico-mail"/></svg><div><b>Email</b>dunholt@harlowvectors.example</div></div>
      <div class="contact-row"><svg><use href="#ico-phone"/></svg><div><b>Call</b>+00 0100 000 227</div></div>
    </div>
    <div class="d-office" style="left:537px">
      <h3>KORVANE OFFICE</h3>
      <div class="contact-row"><svg><use href="#ico-pin"/></svg><div><b>Location</b>9 Marlow Quay, Level 12<br>Korvane, Suite 12B</div></div>
      <div class="contact-row"><svg><use href="#ico-mail"/></svg><div><b>Email</b>korvane@harlowvectors.example</div></div>
      <div class="contact-row"><svg><use href="#ico-phone"/></svg><div><b>Call</b>+00 0100 000 948</div></div>
    </div>
    <div class="btn btn--mauve">Contact us</div>
  </section>

  <footer class="d-section d-footer">
    <div class="wordmark"><i></i>Harlow Vectors</div>
    <p class="blurb">Lorem ipsum is simply dummy text of the printing and typesetting industry.</p>
    <div class="social"><i></i><i></i><i></i></div>
    <small>© 2024. All rights reserved.</small>
    <ul class="d-links"><li>LINKS</li><li>Approach</li><li>Businesses</li><li>Insights</li><li>Careers</li><li>Contact us</li></ul>
  </footer>

  <form class="d-touch">
    <h3>GET IN TOUCH</h3>
    <div class="field">Full name</div>
    <div class="field">Email address</div>
    <div class="field">Subject</div>
    <div class="field field--area">Message<svg viewBox="0 0 12 12"><use href="#ico-send"/></svg></div>
  </form>
</main>

<main class="mobile">

  <header class="m-section m-nav">
    <div class="m-burger"></div>
    <div class="wordmark"><i></i>Harlow Vectors</div>
    <svg width="9" height="9" viewBox="0 0 12 12" fill="none" stroke="#333" stroke-width="1.4"><circle cx="6" cy="4" r="2.5"/><path d="M1.5 11.5c.5-3 2.3-4 4.5-4s4 1 4.5 4"/></svg>
  </header>

  <section class="m-section m-hero">
    <div class="photo photo--globe" role="img" aria-label="Glowing digital globe made of blue light points"></div>
    <div class="eyebrow">Harlow Vectors</div>
    <h1>BRINGING AI AND<br>STATISTICAL<br>INFERENCE TO<br>FINANCIAL<br>MARKETS</h1>
    <p>Harlow Vectors is a quantitative asset manager with the singular focus of delivering algorithmic strategies that work</p>
    <div class="btn btn--blue">Contact us</div>
    <div class="d-scroll-line"></div>
  </section>

  <section class="m-section m-photo">
    <div class="photo photo--suit" role="img" aria-label="Businessman in a dark suit holding a tablet with a glowing rising bar chart"></div>
  </section>

  <section class="m-section m-who">
    <h2 class="head">Who we are</h2>
    <p>We deliver consistent alpha across liquid markets through the application of proprietary IP in Bayesian inference, machine learning and artificial intelligence. We are a multi-disciplinary team founded by experienced finance professionals from premier institutions, leading academics from the Thornbury Stellar Unit at Ashmere College and world-class software engineers.</p>
    <div class="btn btn--mauve">Read more</div>
  </section>

  <section class="m-section m-stats">
    <div class="stats-box">
      <div class="stat" style="top:34px"><b>200+</b><span>Team members</span></div>
      <div class="stat" style="top:124px"><b>15+</b><span>Year history</span></div>
      <div class="stat" style="top:214px"><b>100+</b><span>Portfolio managers</span></div>
    </div>
  </section>

  <section class="m-section m-values">
    <div class="eyebrow">Company</div>
    <h2 class="head">Values</h2>
    <p>Our logo portrays a silhouette of the lattice walkway at Ashmere College.</p>
  </section>

  <section class="m-section m-approach">
    <h2>APPROACH</h2>
    <p>Our unique scientific approach allows us to bridge cutting-edge mathematical research and computing expertise with financial knowledge to bring algorithms that work to liquid markets</p>
    <svg class="m-arrow" style="left:10px" viewBox="0 0 10 14"><path d="M8 1L2 7l6 6"/></svg>
    <div class="tile tile--active"><svg width="26" height="22" viewBox="0 0 26 22"><path d="M6 14a5 5 0 0 1 1-9.8A7 7 0 0 1 20 6a4 4 0 0 1 0 8z"/><path d="M9 14v5M13 14v6M17 14v5"/></svg>It starts with<br>data</div>
    <svg class="m-arrow" style="right:10px" viewBox="0 0 10 14"><path d="M2 1l6 6-6 6"/></svg>
    <div class="btn btn--blue">Find out how we do it</div>
  </section>

  <section class="m-section m-culture">
    <h2 class="head">Culture</h2>
    <p class="lead">We prioritise having a company culture that promotes sharing ideas in a safe, collaborative research environment. We make sure that every member of the team has the opportunity to explore their own ideas through weekly 'innovation time', and ensure that everyone gets the support they need to continue to grow as individuals within the company.</p>
    <div class="photo photo--handshake" role="img" aria-label="Two business people shaking hands in a bright office"></div>
    <div class="photo photo--chart" role="img" aria-label="Glowing candlestick stock chart on a dark blue screen"></div>
    <p class="body">Lorem ipsum is simply dummy text of the printing and typesetting industry. Lorem Ipsum has been the industry's standard dummy text ever since the 1500s, when an unknown printer took a galley of type and scrambled it to make a type specimen book. It has survived not only five centuries, but also the leap into electronic typesetting, remaining essentially unchanged.</p>
    <div class="btn btn--mauve">Our culture</div>
  </section>

  <section class="m-section m-hiring">
    <div class="photo photo--particles" role="img" aria-label="Flowing wave of blue digital particles on a dark background"></div>
    <div class="card">
      <div class="eyebrow">Working at</div>
      <h2>HARLOW<br>VECTORS</h2>
      <p>We are always looking for exceptional talent to join our entrepreneurial team. We are looking for individuals who are creative thinkers, can demonstrate analytical rigour and are passionate about the intersection of science, finance and technology.</p>
      <div class="btn btn--white">Connect with us</div>
    </div>
  </section>

  <section class="m-section m-insights">
    <div class="eyebrow">Latest</div>
    <h2 class="head">Insights</h2>
    <div class="photo photo--phone" role="img" aria-label="Hands holding a phone in front of a laptop showing a stock chart"></div>
    <div class="m-dot" style="left:14px"><svg viewBox="0 0 6 6"><path d="M4 1L2 3l2 2"/></svg></div>
    <div class="m-dot" style="left:172px"><svg viewBox="0 0 6 6"><path d="M2 1l2 2-2 2"/></svg></div>
    <h3>LOREM IPSUM IS SIMPLY....</h3>
    <p>Lorem ipsum is simply dummy text of the printing and typesetting industry. Lorem ipsum has been the industry's standard dummy text ever since the 1500s, when an unknown printer.</p>
  </section>

  <section class="m-section m-partner">
    <h2>PARTNER WITH US</h2>
    <div class="m-office" style="top:84px">
      <h3>EASTMERE OFFICE</h3>
      <div class="contact-row"><svg><use href="#ico-pin"/></svg><div><b>Location</b>42 West Mill Street, 8th Floor<br>Eastmere, Suite 8A</div></div>
      <div class="contact-row"><svg><use href="#ico-mail"/></svg><div><b>Email</b>info@harlowvectors.example</div></div>
      <div class="contact-row"><svg><use href="#ico-phone"/></svg><div><b>Call</b>+00 0100 000 114</div></div>
    </div>
    <div class="m-office" style="top:248px">
      <h3>DUNHOLT OFFICE</h3>
      <div class="contact-row"><svg><use href="#ico-pin"/></svg><div><b>Location</b>18 Fenwick Lane, 3rd Floor<br>Dunholt, Suite 3C</div></div>
      <div class="contact-row"><svg><use href="#ico-mail"/></svg><div><b>Email</b>dunholt@harlowvectors.example</div></div>
      <div class="contact-row"><svg><use href="#ico-phone"/></svg><div><b>Call</b>+00 0100 000 227</div></div>
    </div>
    <div class="m-office" style="top:412px">
      <h3>KORVANE OFFICE</h3>
      <div class="contact-row"><svg><use href="#ico-pin"/></svg><div><b>Location</b>9 Marlow Quay, Level 12<br>Korvane, Suite 12B</div></div>
      <div class="contact-row"><svg><use href="#ico-mail"/></svg><div><b>Email</b>korvane@harlowvectors.example</div></div>
      <div class="contact-row"><svg><use href="#ico-phone"/></svg><div><b>Call</b>+00 0100 000 948</div></div>
    </div>
    <div class="btn btn--mauve">Contact us</div>
  </section>

  <section class="m-section m-touch">
    <form class="box">
      <h3>GET IN TOUCH</h3>
      <div class="field">Full name</div>
      <div class="field">Email address</div>
      <div class="field">Subject</div>
      <div class="field field--area">Message<svg viewBox="0 0 12 12"><use href="#ico-send"/></svg></div>
    </form>
  </section>

  <footer class="m-section m-footer">
    <div class="wordmark"><i></i>Harlow Vectors</div>
    <p class="blurb">Lorem ipsum is simply dummy text of the printing and typesetting industry.</p>
    <ul class="m-links"><li>LINKS</li><li>Approach</li><li>Businesses</li><li>Insights</li><li>Careers</li><li>Contact us</li></ul>
    <div class="social"><i></i><i></i><i></i></div>
    <small>© 2024. All rights reserved.</small>
  </footer>
</main>

</body>
</html>
```